Milo's Sweet Harbor Package Design

A logo has already been made and now i need to incorporate that logo into a package design. Milo's Sweet Harbor products will be sold in retail stores and its package should appeal to both adults and children. Milo's Sweet Harbor sells candy, nuts and other snacks. Files attached will be logo files and pictures of similar package. Please refer to the files for package design. The physical package consists of a printed card (5.75 inches X 4 inches) and a plastic bag. The card is folded over the plastic bag, sealed and hole punched. The design on the card(5.75 inches X 4 inches) should consist of the logo, price(in this case it is $1.99 however it will vary for other products) and product type (in this case its apple(however it will change for other products). On the "back side"(the card is folded down the middle over the plastic and the top of the card becomes the back side, notice how in the example the top half is upside down, this is correct) should include nutrition facts, ingredients, a UPC barcode and the company information(again these vary depending on the product except for the company information that will be same for all products. Company info - "Packaged & Distributed By: Brightfield Confection Supply
7214 Hollander Rd Suite 308 Sterling Heights, Michigan 48257 586-555-3197"

TO WHOEVER WINS THE CONTEST WE WILL COMMISSION YOU TO USE THE SAME DESIGN AND ADD THE NECESSARY INFORMATION(upc, ingredients list, nutritional facts, etc) FOR THE MULTIPLE FLAVORS THAT WE WILL BE PRODUCING UNDER THE Milo's Sweet Harbor BRAND.

```html
<!DOCTYPE html>
<html lang="en">
<head>
<meta charset="utf-8">
<title>Milo's Sweet Harbor – Header Card</title>
<link rel="stylesheet" href="https://fonts.googleapis.com/css2?family=Arimo:wght@400;700&family=Archivo+Black&family=Roboto+Slab:wght@700&display=swap">
<style>
  :root{
    --stage:#5c5c5e;
    --card-pink:#f7bcd6;
    --card-light:#fde3ef;
    --drip-deep:#e8395f;
    --drip-light:#f98aa2;
    --ink:#000;
    --ingredient:#c2185b;
    --brand:#b4245a;
    --price:#d81b60;
    --badge:#fde6ef;
    --badge-edge:#f3a6c2;
    --white:#fff;
  }
  *{box-sizing:border-box;margin:0;padding:0}
  html,body{width:1200px;height:892px;overflow:hidden;background:var(--stage)}
  .header-card{
    position:absolute;left:92px;top:93px;width:1017px;height:707px;overflow:hidden;
    background:radial-gradient(ellipse at 50% 50%,var(--card-light) 0%,var(--card-pink) 75%);
    box-shadow:6px 8px 18px rgba(0,0,0,.35);
    font-family:"Arimo",Arial,sans-serif;
  }
  .drip-band{position:absolute;left:0;top:230px;width:1017px;height:220px}
  .hang-holes{position:absolute;left:0;top:0;width:1017px;height:707px}
  .back-panel{position:absolute;left:0;top:0;width:1017px;height:353px;transform:rotate(180deg)}
  .nutrition-facts{
    position:absolute;left:747px;top:17px;width:222px;height:320px;background:var(--white);
    padding:5px;color:var(--ink);
  }
  .nf-frame{border:1px solid var(--ink);height:100%;padding:3px 5px;font-size:8.5px;line-height:1.3;overflow:hidden}
  .nf-title{display:flex;justify-content:space-between;font-family:"Archivo Black",Arial,sans-serif;font-size:21px;line-height:1.05}
  .nf-row{display:flex;justify-content:space-between;border-top:.6px solid var(--ink);padding:1.5px 0}
  .nf-row.noline{border-top:none}
  .nf-serving{font-weight:700;font-size:10px;border-bottom:6px solid var(--ink);padding-bottom:2px}
  .nf-calories{display:flex;justify-content:space-between;align-items:flex-end;font-family:"Archivo Black",Arial,sans-serif;font-size:17px;line-height:1;border-bottom:4px solid var(--ink);padding-bottom:2px}
  .nf-calories .num{font-size:24px}
  .nf-dv{text-align:right;font-size:6px;font-weight:700;padding:1px 0}
  .indent{padding-left:8px}
  .indent2{padding-left:16px}
  .nf-end{border-bottom:5px solid var(--ink)}
  .nf-note{font-size:6px;line-height:1.3;padding-top:3px}
  .upc-space{position:absolute;left:370px;top:185px;width:285px;height:132px;background:var(--white)}
  .ingredients{
    position:absolute;left:39px;top:147px;color:var(--ingredient);font-size:16px;line-height:21.5px;white-space:nowrap;
  }
  .brand-dot{position:absolute;left:199px;top:480px;width:52px;height:52px;border-radius:50%;background:var(--brand)}
  .brand-name{
    position:absolute;left:60px;top:548px;width:330px;text-align:center;
    font-family:"Arimo",Arial,sans-serif;font-weight:700;font-size:40px;line-height:1.1;color:var(--brand);
  }
  .candy-art{
    position:absolute;left:436px;top:450px;width:520px;height:257px;border-radius:60% 60% 0 0/45% 45% 0 0;
    background:radial-gradient(ellipse at 40% 60%,#f5a04a 0%,#f06a6a 35%,#e8476f 60%,rgba(247,188,214,0) 85%);
  }
  .price-badge{
    position:absolute;left:894px;top:592px;width:124px;height:124px;border-radius:50%;
    background:var(--badge);border:2px dashed var(--badge-edge);
    display:flex;align-items:center;justify-content:center;
  }
  .price{font-family:"Roboto Slab",Georgia,serif;font-weight:700;font-size:30px;color:var(--price);transform:rotate(-6deg);margin-top:-14px}
</style>
</head>
<body>
<main class="header-card">
  <svg class="drip-band" viewBox="0 0 1017 220" preserveAspectRatio="none" aria-hidden="true">
    <defs>
      <linearGradient id="dripFill" x1="0" y1="0" x2="0" y2="1">
        <stop offset="0" stop-color="#f98aa2"/>
        <stop offset=".5" stop-color="#e8395f"/>
        <stop offset="1" stop-color="#f98aa2"/>
      </linearGradient>
    </defs>
    <path fill="url(#dripFill)" d="M0 60 C40 40 70 70 110 50 C150 20 180 70 230 55 C280 40 300 70 340 45 C380 10 410 60 450 40 C500 15 520 55 560 40 C600 20 640 10 690 40 C730 60 760 30 800 25 C840 20 860 55 900 45 C940 35 980 50 1017 40 L1017 180 C980 170 940 185 900 175 C860 165 840 200 800 195 C760 190 730 160 690 180 C640 210 600 200 560 180 C520 165 500 205 450 180 C410 160 380 210 340 175 C300 150 280 180 230 165 C180 150 150 200 110 170 C70 150 40 180 0 160 Z"/>
    <line x1="0" y1="123" x2="1017" y2="123" stroke="#e8395f" stroke-width="1.5"/>
  </svg>

  <svg class="hang-holes" viewBox="0 0 1017 707" aria-hidden="true">
    <path fill="#fff" stroke="#555" stroke-width="1" d="M440 275 H576 A18 18 0 0 1 576 311 H548 C540 326 525 331 508 331 C491 331 476 326 468 311 H440 A18 18 0 0 1 440 275 Z"/>
    <path fill="#fff" stroke="#555" stroke-width="1" d="M440 431 H576 A18 18 0 0 0 576 395 H548 C540 380 525 373 508 373 C491 373 476 380 468 395 H440 A18 18 0 0 0 440 431 Z"/>
  </svg>

  <section class="back-panel">
    <div class="nutrition-facts">
      <div class="nf-frame">
        <div class="nf-title"><span>Nutrition</span><span>Facts</span></div>
        <div class="nf-row noline" style="font-size:9.5px">6 servings per container</div>
        <div class="nf-row noline nf-serving"><span>Serving size</span><span>10 pcs (10g)</span></div>
        <div class="nf-row noline" style="font-weight:700">Amount Per Serving</div>
        <div class="nf-calories"><span>Calories</span><span class="num">110</span></div>
        <div class="nf-dv">% Daily Value*</div>
        <div class="nf-row"><span><b>Total Fat</b> 2.5g</span><span>3%</span></div>
        <div class="nf-row indent"><span>Saturated Fat 1g</span><span>5%</span></div>
        <div class="nf-row indent"><span><i>Trans</i> Fat 0g</span><span></span></div>
        <div class="nf-row"><span><b>Sodium</b> 10mg</span><span>0%</span></div>
        <div class="nf-row"><span><b>Total Carbohydrate</b> 22g</span><span>8%</span></div>
        <div class="nf-row indent"><span>Dietary Fiber 0g</span><span>0%</span></div>
        <div class="nf-row indent"><span>Total Sugars 16g</span><span></span></div>
        <div class="nf-row indent2"><span>Includes 0g Added Sugars</span><span>0%</span></div>
        <div class="nf-row nf-end"><span><b>Protein</b> 0g</span><span>0%</span></div>
        <p class="nf-note">Not a significant source of cholesterol, vitamin D, calcium, iron, and potassium</p>
        <p class="nf-note">* The % Daily Value (DV) tells you how much a nutrient in a serving of food contributes to a daily diet. 2,000 calories a day is used for general nutrition advice.</p>
      </div>
    </div>
    <div class="upc-space"></div>
    <p class="ingredients">Ingredients: Lorem dolor amet,<br>consectetuer adipiscing elit, sed<br>diam nonummy nibh euismod<br>tincidunt ut laoreet aliquam . Ut wisi<br>enim ad minim veniam, &nbsp;Lorem<br>ipsum dolor sit amet, consectetuer<br>adipiscing elit,magna aliquam<br>volutpat. Ut wisi enim ad veniam.</p>
  </section>

  <div class="brand-dot"></div>
  <h1 class="brand-name">Milo's Sweet Harbor</h1>

  <div class="candy-art" role="img" aria-label="Illustration of assorted lollipops, swirl candies and candy canes"></div>

  <div class="price-badge"><span class="price">$1.99</span></div>
</main>
</body>
</html>
```